Website design for headhunting agency

The design I need (PSD file) is for a company offering specialised services in recruitment of high-end executive and management positions for businesses.
OBJECTIVES OF THE WEBSITE:
1. Let entrepreneurs and business leaders know about their services and easily have them contact Varolinq if they want more information about their services.
2. Display a list of available carreer opportunities (according to their client's need).
WHAT I NEED:
1st, I need the design for the Home Page ONLY. Once approved, I will need the other pages designed as well. (Here is prototype that we've already developed for the Website that will guide you in the design:
http://demo.pelvarshop.net/varolinq/fr/accueil)
ATTACHED FILES
- Logo
- PDF brochure: Use for inspiration. It is encouraged that you use pictures from this brochure. You can always suggest new ones, as long as they are not expensive to buy and have the same look and feel as the brochure.
HOMEPAGE:
1. Main menu : 6 sections
Accueil | Varolinq | Équipe | Approche | Postes disponibles | Publications
2. Main slider: 4 sections
- Chasseurs de têtes (Headhunters)
- Notre approche (Our Approach)
- Postes cadres disponibles (Executive Careers
Opportunities)
- Contactez-nous (Contact Us)
3. Main Call To Action Boxes :
- Liste Des postes disponibles (Liste of Available Careers
Opportunities)
- Formulaire de contact (contact form)
4. Latest blog articles
- Les derniers articles.
OTHER PAGES (to design once Homepage is approved)
- Varolinq (about us)
- Équipe (our team)
- Approche (our approach)
- Postes disponibles (Career opportunities)
- Publications (blog articles)
- Contact (Contact us)
Target Market(s)
ORGANIZATIONS:
Leaders of organizations seeking to recruit highly qualified staff.
HIGHLY QUALIFIED RESOURCES:
Senior individuals seeking a salary between $70,000 and $ $200,000 annually
PROFESSIONAL SECTORS:
manufacturing : Primary and secondary industries
pharmaceutical
Aerospace
Finances
Retail business
Engineering
Chemical and petrochemical
IT, telecommunications and high technology
Professional Organizations and Association
Industry/Entity Type
Business
Look and feel
Each slider illustrates characteristics of the customer's brand and the style your logo design should communicate.

```html
<!DOCTYPE html>
<html lang="fr">
<head>
<meta charset="utf-8">
<title>Varolinq – Recherche de cadres</title>
<link href="https://fonts.googleapis.com/css2?family=Open+Sans:wght@400;600;700&display=swap" rel="stylesheet">
<style>
:root{
  --teal-dark:#0b5560;
  --teal:#116a76;
  --teal-text:#15606c;
  --panel:#78abaa;
  --panel-soft:#8dbab8;
  --orange:#e89a1c;
  --ink:#1d1d1d;
  --grey:#8a8a8a;
  --line:#d6d6d6;
  --white:#ffffff;
}
*{box-sizing:border-box;margin:0;padding:0}
html,body{width:703px;height:1200px;overflow:hidden;background:var(--white)}
body{font-family:"Open Sans",Arial,sans-serif;color:var(--ink)}
.page{position:relative;width:703px;height:1200px;overflow:hidden;background:var(--white)}
.abs{position:absolute}

/* top utility bar */
.topbar{left:0;top:0;width:703px;height:24px;background:linear-gradient(#1b7480,#0a4e58)}
.topbar ul{list-style:none;display:flex;position:absolute;right:0;top:0;height:24px}
.topbar li{height:24px;line-height:24px;font-size:10px;font-weight:700;color:var(--white);letter-spacing:.3px;text-align:center;border-left:1px solid rgba(255,255,255,.35)}
.topbar li:nth-child(1){width:88px}
.topbar li:nth-child(2){width:103px}
.topbar li:nth-child(3){width:110px}
.topbar li:nth-child(4){width:132px}
.topbar li:nth-child(5){width:90px}

/* header */
.brand{left:18px;top:42px}
.brand-name{display:flex;align-items:center;gap:8px;font-size:29px;font-weight:600;color:var(--teal);letter-spacing:.5px;line-height:1}
.brand-mark{width:14px;height:14px;background:var(--teal)}
.brand-tag{font-size:12px;color:#4b4b4b;margin-left:66px;margin-top:4px}
.mainnav{right:12px;top:62px;display:flex;font-size:12px;font-weight:700;color:var(--teal-text);letter-spacing:.3px}
.mainnav span{padding:0 9px;border-left:1px solid #9bb9bd;line-height:13px}
.mainnav span:first-child{border-left:0}
.mainnav .active{color:var(--orange)}
.header-rule{left:0;top:112px;width:703px;height:1px;background:var(--line)}

/* hero slider */
.hero{left:0;top:113px;width:703px;height:274px;overflow:hidden;background:#f4f6f7}
.hero-photo{position:absolute;left:250px;top:0;width:453px;height:274px;background:radial-gradient(ellipse at 55% 55%,#d9c3b4 0%,#e9e4e1 30%,#f3f4f6 60%,#fbfbfc 100%)}
.hero-panel{position:absolute;left:0;top:0}
.hero-title{left:43px;top:177px;font-size:21px;font-weight:600;color:var(--teal-dark);letter-spacing:.6px}
.hero-text{left:47px;top:218px;width:245px;font-size:10px;line-height:15px;color:var(--white)}
.arrow{top:232px}
.dots{left:325px;top:402px;display:flex;gap:5px}
.dots i{width:9px;height:9px;border-radius:50%;background:#c8c8c8}
.dots i:first-child{background:var(--teal)}
.slider-rule{left:0;top:388px;width:703px;height:1px;background:var(--line)}

/* buttons */
.btn{display:inline-flex;align-items:center;gap:5px;height:23px;padding:0 11px 0 9px;border-radius:5px;background:linear-gradient(#4a4a4a,#0b0b0b);color:var(--white);font-size:11px;font-weight:600;border:1px solid #000}
.btn svg{width:7px;height:8px}
.btn-outline{border:1px solid var(--white);background:var(--teal);box-shadow:0 0 0 1px #0d4d56}

/* call to action boxes */
.jobs-box{left:16px;top:434px;width:328px;height:189px;border:1px solid var(--line)}
.contact-box{left:360px;top:434px;width:328px;height:189px;background:var(--panel)}
.box-title{position:absolute;left:10px;top:13px;font-size:13px;font-weight:600;color:var(--ink);letter-spacing:.3px}
.job-list{position:absolute;left:30px;top:43px;list-style:none}
.job-list li{display:flex;align-items:center;gap:13px;height:16.5px;font-size:10.5px;color:var(--teal-text)}
.job-list svg{width:7px;height:8px}
.jobs-box .btn{position:absolute;left:30px;top:152px}
.field-label{position:absolute;left:36px;font-size:11.5px;color:#0f2f33}
.field{position:absolute;left:129px;width:166px;height:21px;background:var(--white)}
.contact-box .btn{position:absolute;left:36px;top:152px;padding:0 16px 0 10px;border-color:#cfe0df}

/* articles */
.articles-rule{left:0;top:640px;width:703px;height:1px;background:var(--line)}
.section-title{left:25px;top:651px;font-size:13px;font-weight:600;letter-spacing:.3px}
.card{width:328px;height:190px;border:1px solid var(--line)}
.card-img{position:absolute;left:10px;top:11px;width:123px;height:80px;border:1px solid #e0e0e0}
.card-intro{position:absolute;left:145px;top:11px;width:172px;font-size:8.5px;line-height:13.4px;color:var(--grey)}
.card-text{position:absolute;left:10px;top:100px;width:308px;font-size:8.5px;line-height:13.4px;color:var(--grey)}
.card .btn{position:absolute;left:10px;top:156px;height:22px}

/* follow / newsletter row */
.follow{top:1110px;display:flex;align-items:center;gap:6px;font-size:13px;color:var(--ink);letter-spacing:.2px}
.follow svg{width:7px;height:8px}
.tag-box{top:1103px;height:35px;border:1px solid var(--line);display:flex;align-items:center;justify-content:center;font-size:15px;font-weight:700;color:var(--teal-text)}

/* footer */
.footer{left:0;top:1169px;width:703px;height:31px;background:linear-gradient(#135f6a,#0a4952);border-top:3px solid #d8e4e5;color:var(--white);font-size:9.5px;display:flex;align-items:center;justify-content:space-between;padding:0 14px 0 26px}
</style>
</head>
<body>
<div class="page">

  <nav class="topbar abs">
    <ul>
      <li>ACCUEIL</li><li>PLAN DU SITE</li><li>CODE D'ÉTIQUE</li><li>CONTACT</li><li>ENGLISH</li>
    </ul>
  </nav>

  <header>
    <div class="brand abs">
      <div class="brand-name"><span class="brand-mark"></span>VAROLINQ</div>
      <div class="brand-tag">Recherche de cadres</div>
    </div>
    <nav class="mainnav abs">
      <span class="active">À PROPOS</span><span>ÉQUIPE</span><span>APPROCHE</span><span>POSTES DISPONIBLES</span><span>PUBLICATIONS</span>
    </nav>
  </header>
  <div class="header-rule abs"></div>

  <section class="hero abs">
    <div class="hero-photo" role="img" aria-label="Photo d'une femme d'affaires souriante au premier plan, avec des silhouettes de collègues floues en arrière-plan"></div>
    <svg class="hero-panel" width="330" height="274" viewBox="0 0 330 274">
      <polygon points="0,0 322,0 266,274 0,274" fill="#4f8e91"/>
      <polygon points="0,0 240,0 290,150 266,274 0,274" fill="#5b9a9b"/>
      <polygon points="240,0 322,0 290,150" fill="#3f7d80"/>
      <polygon points="266,274 322,0 330,0 274,274" fill="#e7eef0"/>
    </svg>
    <svg class="arrow abs" style="left:8px;top:119px" width="14" height="22" viewBox="0 0 14 22"><polyline points="11,2 3,11 11,20" fill="none" stroke="#c9d6d8" stroke-width="4"/></svg>
    <svg class="arrow abs" style="left:680px;top:119px" width="14" height="22" viewBox="0 0 14 22"><polyline points="3,2 11,11 3,20" fill="none" stroke="#5d9a9f" stroke-width="4"/></svg>
  </section>
  <h1 class="hero-title abs">CHASSEURS DE TÊTES</h1>
  <p class="hero-text abs">Donec quam felis, ultricies nec, pellentesque eu, pretium quis, sem. Nulla consequat massa quis enim. Donec pede justo, fringilla vel, aliquet nec, vulputate eget, arcu. In enim justo, rhoncus ut, imperdiet a, venenatis vitae, justo.</p>
  <span class="btn btn-outline abs" style="left:43px;top:323px"><svg viewBox="0 0 7 8"><polygon points="0,0 7,4 0,8" fill="#fff"/></svg>View More</span>
  <div class="slider-rule abs"></div>
  <div class="dots abs"><i></i><i></i><i></i><i></i></div>

  <section class="jobs-box abs">
    <h2 class="box-title">LISTE DES POSTES DISPONIBLES</h2>
    <ul class="job-list">
      <li><svg viewBox="0 0 7 8"><polygon points="0,0 7,4 0,8" fill="#222"/></svg>Aonecqua mfelisuame</li>
      <li><svg viewBox="0 0 7 8"><polygon points="0,0 7,4 0,8" fill="#222"/></svg>Bonecqua mfeluame</li>
      <li><svg viewBox="0 0 7 8"><polygon points="0,0 7,4 0,8" fill="#222"/></svg>Conecqua mame</li>
      <li><svg viewBox="0 0 7 8"><polygon points="0,0 7,4 0,8" fill="#222"/></svg>Doneiua feuame</li>
      <li><svg viewBox="0 0 7 8"><polygon points="0,0 7,4 0,8" fill="#222"/></svg>Enecqua rhlisuame</li>
      <li><svg viewBox="0 0 7 8"><polygon points="0,0 7,4 0,8" fill="#222"/></svg>FAonecqua yrelisume</li>
    </ul>
    <span class="btn"><svg viewBox="0 0 7 8"><polygon points="0,0 7,4 0,8" fill="#fff"/></svg>View More</span>
  </section>

  <section class="contact-box abs">
    <h2 class="box-title">FORMULAIRE DE CONTACT</h2>
    <span class="field-label" style="top:66px">User Name</span>
    <span class="field" style="top:64px"></span>
    <span class="field-label" style="top:110px">Password</span>
    <span class="field" style="top:108px"></span>
    <span class="btn"><svg viewBox="0 0 7 8"><polygon points="0,0 7,4 0,8" fill="#fff"/></svg>Login</span>
  </section>

  <div class="articles-rule abs"></div>
  <h2 class="section-title abs">LES DERNIERS ARTICLES</h2>

  <article class="card abs" style="left:16px;top:675px">
    <div class="card-img" role="img" aria-label="Photo d'une réunion d'affaires autour d'une table" style="background:linear-gradient(135deg,#f1ece6,#c9b39d 55%,#6f5a48)"></div>
    <p class="card-intro">Donec quam felis, ultricies nec, pellentesque eu, pretium quis, sem. Nulla consequat massa quis enim. Donec pede justo, fringilla vel, aliquet nec, vulputate eget, arcu.</p>
    <p class="card-text">Donec quam felis, ultricies nec, pellentesque eu, pretium quis, sem. Nulla consequat massa quis enim. Donec pede justo, fringilla vel, aliquet nec, vulputate eget, arcu.</p>
    <span class="btn"><svg viewBox="0 0 7 8"><polygon points="0,0 7,4 0,8" fill="#fff"/></svg>View More</span>
  </article>

  <article class="card abs" style="left:360px;top:675px">
    <div class="card-img" role="img" aria-label="Photo de plans techniques enroulés sur un bureau" style="background:linear-gradient(135deg,#fafafa,#dfe4e8 55%,#9fb4c4)"></div>
    <p class="card-intro">Donec quam felis, ultricies nec, pellentesque eu, pretium quis, sem. Nulla consequat massa quis enim. Donec pede justo, fringilla vel, aliquet nec, vulputate eget, arcu.</p>
    <p class="card-text">Donec quam felis, ultricies nec, pellentesque eu, pretium quis, sem. Nulla consequat massa quis enim. Donec pede justo, fringilla vel, aliquet nec, vulputate eget, arcu.</p>
    <span class="btn"><svg viewBox="0 0 7 8"><polygon points="0,0 7,4 0,8" fill="#fff"/></svg>View More</span>
  </article>

  <article class="card abs" style="left:16px;top:883px">
    <div class="card-img" role="img" aria-label="Photo de professionnels en discussion" style="background:linear-gradient(135deg,#efe7dd,#c79f7e 50%,#5a4235)"></div>
    <p class="card-intro">Donec quam felis, ultricies nec, pellentesque eu, pretium quis, sem. Nulla consequat massa quis enim. Donec pede justo, fringilla vel, aliquet nec, vulputate eget, arcu.</p>
    <p class="card-text">Donec quam felis, ultricies nec, pellentesque eu, pretium quis, sem. Nulla consequat massa quis enim. Donec pede justo, fringilla vel, aliquet nec, vulputate eget, arcu.</p>
    <span class="btn"><svg viewBox="0 0 7 8"><polygon points="0,0 7,4 0,8" fill="#fff"/></svg>View More</span>
  </article>

  <article class="card abs" style="left:360px;top:883px">
    <div class="card-img" role="img" aria-label="Photo de collègues travaillant dans un bureau lumineux" style="background:linear-gradient(135deg,#f4f6f7,#c6d0d5 55%,#4d5a62)"></div>
    <p class="card-intro">Donec quam felis, ultricies nec, pellentesque eu, pretium quis, sem. Nulla consequat massa quis enim. Donec pede justo, fringilla vel, aliquet nec, vulputate eget, arcu.</p>
    <p class="card-text">Donec quam felis, ultricies nec, pellentesque eu, pretium quis, sem. Nulla consequat massa quis enim. Donec pede justo, fringilla vel, aliquet nec, vulputate eget, arcu.</p>
    <span class="btn"><svg viewBox="0 0 7 8"><polygon points="0,0 7,4 0,8" fill="#fff"/></svg>View More</span>
  </article>

  <div class="follow abs" style="left:24px"><svg viewBox="0 0 7 8"><polygon points="0,0 7,4 0,8" fill="#116a76"/></svg>SUIVEZ-NOUS SUR NEXALINK</div>
  <div class="tag-box abs" style="left:217px;width:88px">Nexalink</div>
  <div class="follow abs" style="left:368px"><svg viewBox="0 0 7 8"><polygon points="0,0 7,4 0,8" fill="#116a76"/></svg>INSCRIVEZ-VOUS À L'INFOLETTRE</div>
  <div class="tag-box abs" style="left:599px;width:88px;font-size:17px">Sign Up</div>

  <footer class="footer abs">
    <span>© Varolinq - Tous droits réservés</span>
    <span>Site Web et stratégie Agence de Développement Internet</span>
  </footer>

</div>
</body>
</html>
```